Natural Light/Organic/Documentary Photography Business

I like a simple, approachable, feminine, earthy/organic feel. Earth/neutral tones, nothing too loud or obnoxious. I like the watercolor look. I don't want anything too trendy or something I'll get tired of after a couple months. As far as colors, I am much more a fan of cream/taupe/blue/green...not a fan of pink or purple at all.

Target Market(s)

Weddings & Families

Industry/Entity Type

Wedding Photography

Contact Information for Business Card

website, email, phone number

Font styles to use
Other font styles liked:
• Horizontes, Gotham

Colors

Designer to choose colors to be used in the design.

Requirements
Must have
• Website: www.meliskaverholt.com
• Phone: 482.319.6047
• Email: tessa@meliskaverholt.com
Nice to have
• I like the watercolor look but its not necessary. I like simple/earthy tones. Nothing too loud or distracting. Simple & feminine without being too girly. I like an approachable/soft feel.
• Instagram: www.instagram.com/meliskaverholtphotography/
Should not have
• NO loud colors or design or pattern. I do not want a photo of a camera or lens or anything cheesy like that.

```html
<!DOCTYPE html>
<html lang="en">
<head>
<meta charset="utf-8">
<title>Tessa Meliskaverholt – Business Card</title>
<link rel="stylesheet" href="https://fonts.googleapis.com/css2?family=Open+Sans:wght@400;600&display=swap">
<style>
  :root {
    --backdrop: #ebebeb;
    --paper: #ffffff;
    --taupe: #8e8077;
    --ink: #4a4a4a;
    --on-taupe: #ffffff;
  }
  * { margin: 0; padding: 0; box-sizing: border-box; }
  html, body {
    width: 1200px; height: 799px; overflow: hidden;
    background: var(--backdrop);
    font-family: "Open Sans", Arial, sans-serif;
  }
  .canvas { position: relative; width: 1200px; height: 799px; }
  .card {
    position: absolute; left: 313px; width: 584px; height: 333px; overflow: hidden;
  }
  .card--front { top: 51px; background: var(--paper); }
  .card--back { top: 413px; background: var(--taupe); }

  .brand-name {
    position: absolute; right: 36px; top: 62px;
    font-size: 21px; font-weight: 400; color: var(--taupe); letter-spacing: 0.5px;
  }
  .holder-name {
    position: absolute; left: 37px; top: 212px;
    font-size: 20px; font-weight: 600; color: var(--taupe);
  }
  .rule {
    position: absolute; left: 41px; top: 243px; width: 496px; height: 1px; background: var(--taupe);
  }
  .contacts { position: absolute; left: 38px; top: 251px; list-style: none; }
  .contacts li {
    display: flex; align-items: center; height: 19px;
    font-size: 14px; color: var(--ink);
  }
  .contacts svg { width: 14px; height: 14px; margin-right: 9px; fill: var(--taupe); flex: none; }
  .footer-band { position: absolute; left: 0; bottom: 0; width: 584px; height: 29px; }
  .footer-url {
    position: absolute; right: 32px; bottom: 5px;
    font-size: 14px; color: var(--on-taupe);
  }

  .back-name {
    position: absolute; left: 0; right: 0; top: 146px; text-align: center;
    font-size: 30px; font-weight: 400; color: var(--on-taupe); letter-spacing: 1px;
  }
  .back-url {
    position: absolute; left: 0; right: 0; top: 276px; text-align: center;
    font-size: 15px; color: var(--on-taupe); letter-spacing: 3.4px;
  }
</style>
</head>
<body>
<main class="canvas">
  <section class="card card--front" aria-label="Business card front">
    <p class="brand-name">Tessa Meliskaverholt</p>
    <h1 class="holder-name">Tessa Meliskaverholt</h1>
    <div class="rule"></div>
    <ul class="contacts">
      <li>
        <svg viewBox="0 0 16 16" aria-hidden="true"><path d="M1 6c0-2 3-3.5 7-3.5S15 4 15 6v1.5h-3.5V6h-7v1.5H1z"/><path d="M3.5 8.5 6 6.5h4l2.5 2V14h-9z"/></svg>
        482.319.6047
      </li>
      <li>
        <svg viewBox="0 0 16 16" aria-hidden="true"><path d="M1.5 3.5h13v1.2L8 9 1.5 4.7z"/><path d="M1.5 6.2 8 10.5l6.5-4.3v6.3h-13z"/></svg>
        tessa@meliskaverholt.com
      </li>
      <li>
        <svg viewBox="0 0 16 16" aria-hidden="true"><rect x="2" y="2" width="12" height="12" rx="2"/></svg>
        meliskaverholtphotography
      </li>
    </ul>
    <svg class="footer-band" viewBox="0 0 584 29" aria-hidden="true">
      <path d="M0 15.5H352q10 0 18-13.5" fill="none" stroke="var(--taupe)" stroke-width="2"/>
      <path d="M372 0H584V29H0V22.5H352q12 0 20-22.5z" fill="var(--taupe)"/>
    </svg>
    <p class="footer-url">www.meliskaverholt.com</p>
  </section>

  <section class="card card--back" aria-label="Business card back">
    <p class="back-name">Tessa Meliskaverholt</p>
    <p class="back-url">WWW.MELISKAVERHOLT.COM</p>
  </section>
</main>
</body>
</html>
```